Product Image Design: Climbing Past the Ceiling That Held You Back (Plus More!)

I need a product image designed for a new product I will be selling on sellvanta.com that teaches how to quickly make more money by getting a raise or promotion.

Dimensions must be 1280 x 720 pixels. The product title and subtitle are as follows:

Title: Climbing Past the Ceiling That Held You Back at Last (Plus More!)

Subtitle: A Quick Route to Bigger Salary Jumps Minus Costly Schooling or Flattering the Manager Above You

I'm looking for a design that is eye catching and communicates the idea of business success and getting paid more money from a company or employer.

The target audience is professional men in their 20s and 30s who are looking to quickly make more money and advance in their careers.

Target Market(s)

Professional men in their 20s and 30s who are looking to quickly make more money and advance in their careers.

Industry/Entity Type

Professional Service

Font styles to use
Serif

Requirements
Must have
• Title and subtitle provided in project description.

Final design in 1280 x 720 dimensions (or larger with same width to height ratio).

Eye catching font, colors and graphics, but not overly flashy.

Masculine colors (i.e. no pinks or other feminine colors).
Nice to have
• N/A
Should not have
• Feminine colors or images of women.

```html
<!DOCTYPE html>
<html lang="en">
<head>
<meta charset="utf-8">
<title>Climbing Past the Ceiling That Held You Back at Last (Plus More!)</title>
<link rel="stylesheet" href="https://fonts.googleapis.com/css2?family=Playfair+Display:wght@700;900&family=Libre+Baskerville:wght@400;700&display=swap">
<style>
  :root {
    --page-bg: #050806;
    --bg-deep: #020603;
    --bg-mid: #0b2a12;
    --bg-glow: #174d22;
    --green-bright: #1fc83a;
    --green-mid: #1f7a2c;
    --green-dark: #0f3a17;
    --line-pale: #b9c9b6;
    --text-white: #f4f6f3;
    --silver-light: #ffffff;
    --silver-mid: #c9cccb;
    --silver-dark: #8a8f8d;
  }
  * { margin: 0; padding: 0; box-sizing: border-box; }
  html, body {
    width: 1200px;
    height: 733px;
    overflow: hidden;
    background: var(--page-bg);
  }
  .product-image {
    position: absolute;
    left: 0;
    top: 29px;
    width: 1200px;
    height: 675px;
    overflow: hidden;
    background:
      radial-gradient(ellipse 70% 60% at 35% 50%, var(--bg-glow) 0%, var(--bg-mid) 40%, var(--bg-deep) 85%);
  }
  .money-rain {
    position: absolute;
    left: 720px;
    top: 0;
    width: 480px;
    height: 185px;
    background: radial-gradient(ellipse at 60% 30%, rgba(40,110,45,0.45), rgba(20,60,25,0) 70%);
  }
  .arrow-field {
    position: absolute;
    left: 960px;
    top: 405px;
    width: 240px;
    height: 270px;
    background: radial-gradient(ellipse at 60% 60%, rgba(25,90,35,0.4), rgba(10,40,15,0) 70%);
  }
  .growth-chart, .subtitle-path {
    position: absolute;
    left: 0;
    top: 0;
  }
  .title {
    position: absolute;
    left: 40px;
    font-family: "Playfair Display", serif;
    font-weight: 900;
    text-transform: uppercase;
    line-height: 1;
    background: linear-gradient(180deg, var(--silver-light) 0%, var(--silver-mid) 45%, var(--silver-dark) 55%, var(--silver-light) 100%);
    -webkit-background-clip: text;
    background-clip: text;
    color: transparent;
    filter: drop-shadow(2px 3px 2px rgba(0,0,0,0.85));
    white-space: nowrap;
  }
  .title-lead { top: 50px; font-size: 38px; font-weight: 700; letter-spacing: 3px; }
  .title-line-1 { top: 104px; font-size: 66px; letter-spacing: 1px; }
  .title-line-2 { top: 184px; font-size: 66px; letter-spacing: 1px; }
  .subtitle {
    position: absolute;
    font-family: "Libre Baskerville", serif;
    color: var(--text-white);
    text-transform: uppercase;
    white-space: nowrap;
    line-height: 1.2;
  }
  .subtitle-lead { left: 94px; top: 372px; font-size: 21px; }
  .subtitle-main {
    left: 94px; top: 424px; font-size: 42px; font-weight: 700; letter-spacing: 1px;
    background: linear-gradient(180deg, var(--silver-light) 0%, var(--silver-mid) 50%, var(--silver-dark) 60%, var(--silver-light) 100%);
    -webkit-background-clip: text;
    background-clip: text;
    color: transparent;
    filter: drop-shadow(2px 3px 2px rgba(0,0,0,0.9));
  }
  .subtitle-tail { left: 94px; top: 519px; font-size: 17px; }
  .money-bag {
    position: absolute;
    left: 856px;
    top: 527px;
    width: 66px;
    height: 92px;
    border-radius: 45% 45% 40% 40%;
    background: radial-gradient(circle at 45% 60%, #dfe6de, #8fa08e 80%);
  }
</style>
</head>
<body>
<main class="product-image">
  <div class="money-rain" role="img" aria-label="Falling dollar bills"></div>
  <div class="arrow-field" role="img" aria-label="Faint pattern of upward arrows"></div>

  <svg class="growth-chart" width="1200" height="675" viewBox="0 0 1200 675" aria-hidden="true">
    <defs>
      <linearGradient id="barFade" x1="0" y1="0" x2="0" y2="1">
        <stop offset="0" stop-color="var(--green-mid)" stop-opacity="0.55"/>
        <stop offset="1" stop-color="var(--green-dark)" stop-opacity="0"/>
      </linearGradient>
      <linearGradient id="barBright" x1="0" y1="0" x2="0" y2="1">
        <stop offset="0" stop-color="var(--green-bright)"/>
        <stop offset="1" stop-color="var(--green-dark)" stop-opacity="0"/>
      </linearGradient>
    </defs>
    <g class="bars">
      <rect x="790" y="421" width="13" height="179" fill="url(#barBright)"/>
      <rect x="815" y="451" width="13" height="149" fill="url(#barFade)"/>
      <rect x="838" y="460" width="13" height="140" fill="url(#barFade)"/>
      <rect x="862" y="483" width="13" height="117" fill="url(#barFade)"/>
      <rect x="885" y="471" width="13" height="129" fill="url(#barFade)"/>
      <rect x="909" y="446" width="13" height="154" fill="url(#barFade)"/>
      <rect x="932" y="455" width="13" height="145" fill="url(#barFade)"/>
      <rect x="956" y="432" width="13" height="168" fill="url(#barFade)"/>
      <rect x="979" y="405" width="13" height="195" fill="url(#barFade)"/>
      <rect x="1003" y="391" width="13" height="209" fill="url(#barFade)"/>
      <rect x="1026" y="400" width="13" height="200" fill="url(#barFade)"/>
      <rect x="1047" y="380" width="13" height="220" fill="url(#barFade)"/>
      <rect x="1072" y="373" width="13" height="227" fill="url(#barBright)"/>
      <rect x="1095" y="386" width="13" height="214" fill="url(#barFade)"/>
      <rect x="1118" y="351" width="13" height="249" fill="url(#barBright)"/>
      <rect x="1141" y="377" width="13" height="223" fill="url(#barFade)"/>
      <rect x="1164" y="397" width="13" height="203" fill="url(#barFade)"/>
    </g>
    <g class="trend-arrow" fill="var(--green-mid)" opacity="0.85">
      <polygon points="528,463 745,294 790,322 958,228 952,217 1007,208 985,255 978,245 790,342 748,316 542,475"/>
    </g>
  </svg>

  <div class="title title-lead">Climbing Past the Ceiling</div>
  <div class="title title-line-1">That Held You Back</div>
  <div class="title title-line-2">at Last (Plus More!)</div>

  <svg class="subtitle-path" width="1200" height="675" viewBox="0 0 1200 675" aria-hidden="true">
    <path d="M58 368 V405 H780 Q810 405 810 452 Q810 499 780 499 H82 Q48 499 48 530 Q48 561 82 561 H800"
          fill="none" stroke="var(--line-pale)" stroke-width="3.5"/>
    <polygon points="798,551 818,561 798,571" fill="var(--line-pale)"/>
  </svg>

  <div class="subtitle subtitle-lead">A Quick Route to</div>
  <div class="subtitle subtitle-main">Bigger Salary Jumps</div>
  <div class="subtitle subtitle-tail">Minus Costly Schooling or Flattering the Manager Above You</div>

  <div class="money-bag" role="img" aria-label="Money bag with coins"></div>
</main>
</body>
</html>
```